Business cards

Design business cards for our company. Just a straight, business like design with the logo, name, function and contact details

Target Market(s)

We are a innovative technological company active in water treatment

Industry/Entity Type

Water management

Contact Information for Business Card

Name, Function, email, telephone number, link to website

```html
<!DOCTYPE html>
<html lang="en">
<head>
<meta charset="utf-8">
<title>Corvana Flow – Business Cards</title>
<link rel="stylesheet" href="https://fonts.googleapis.com/css2?family=Open+Sans:wght@400;600;700&display=swap">
<style>
  :root {
    --backdrop: #232323;
    --card: #1d1e22;
    --accent: #2a9ad8;
    --text-light: #eef0f2;
    --text-grey: #a7a9ad;
    --silver: #b9bcc0;
  }
  * { box-sizing: border-box; margin: 0; padding: 0; }
  html, body {
    width: 1200px; height: 780px; overflow: hidden;
    background: var(--backdrop);
    font-family: "Open Sans", Arial, sans-serif;
  }
  .sheet {
    width: 1200px; height: 780px;
    display: flex; align-items: center; justify-content: center; gap: 40px;
  }
  .card {
    position: relative;
    width: 540px; height: 309px;
    background: var(--card);
    box-shadow: 0 14px 30px rgba(0,0,0,.45);
    overflow: hidden;
  }
  .brand {
    display: flex; align-items: center; gap: 10px;
    color: var(--accent);
    font-weight: 600;
    font-size: 30px;
    letter-spacing: .5px;
    line-height: 1;
  }
  .brand__dot {
    width: 16px; height: 16px; border-radius: 50%;
    background: currentColor;
  }
  .card--front .brand { position: absolute; top: 34px; left: 36px; }
  .address {
    position: absolute; top: 92px; left: 36px;
    color: var(--text-light); font-size: 14px; line-height: 1.5;
  }
  .contacts {
    position: absolute; top: 160px; left: 36px;
    list-style: none; color: var(--text-light); font-size: 14px; line-height: 1.55;
  }
  .contacts li { display: flex; align-items: center; gap: 9px; }
  .contacts svg { width: 13px; height: 13px; fill: var(--accent); flex: none; }
  .person {
    position: absolute; right: 44px; bottom: 40px; text-align: right;
  }
  .person__name { font-size: 28px; font-weight: 700; line-height: 1.1; }
  .person__first { color: var(--accent); }
  .person__last { color: var(--text-grey); }
  .person__role { color: var(--text-light); font-size: 16px; margin-top: 4px; }
  .edge-band {
    position: absolute; right: 0; bottom: 40px;
    width: 22px; height: 64px; background: var(--accent);
  }
  .card--back { display: flex; align-items: center; justify-content: center; }
  .card--back .brand { color: var(--silver); font-size: 40px; gap: 14px; }
  .card--back .brand__dot { width: 20px; height: 20px; }
</style>
</head>
<body>
<main class="sheet">
  <section class="card card--front" aria-label="Business card front">
    <div class="brand"><span>Corvana Flow</span><span class="brand__dot"></span></div>
    <p class="address">418 Lakeside Ave, Suite 120<br>Riverton, TX 75001</p>
    <ul class="contacts">
      <li><svg viewBox="0 0 24 24"><path d="M6.6 10.8a15.1 15.1 0 0 0 6.6 6.6l2.2-2.2a1 1 0 0 1 1-.25 11.4 11.4 0 0 0 3.6.57 1 1 0 0 1 1 1V20a1 1 0 0 1-1 1A17 17 0 0 1 3 4a1 1 0 0 1 1-1h3.5a1 1 0 0 1 1 1c0 1.25.2 2.45.57 3.57a1 1 0 0 1-.25 1z"/></svg>(555) 014-2236</li>
      <li><svg viewBox="0 0 24 24"><path d="M2 5h20v14H2zm2 2v.5l8 5 8-5V7zm0 2.9V17h16V9.9l-8 5z"/></svg>info@corvanaflow.com</li>
      <li><svg viewBox="0 0 24 24"><path d="M12 2a10 10 0 1 0 0 20 10 10 0 0 0 0-20zm6.9 9h-3a15 15 0 0 0-1.3-5.6A8 8 0 0 1 18.9 11zM12 4.1c.9 1.2 1.8 3.6 1.9 6.9h-3.8c.1-3.3 1-5.7 1.9-6.9zM9.4 5.4A15 15 0 0 0 8.1 11h-3a8 8 0 0 1 4.3-5.6zM5.1 13h3a15 15 0 0 0 1.3 5.6A8 8 0 0 1 5.1 13zm6.9 6.9c-.9-1.2-1.8-3.6-1.9-6.9h3.8c-.1 3.3-1 5.7-1.9 6.9zm2.6-1.3a15 15 0 0 0 1.3-5.6h3a8 8 0 0 1-4.3 5.6z"/></svg>www.corvanaflow.com</li>
    </ul>
    <div class="person">
      <p class="person__name"><span class="person__first">Lena</span> <span class="person__last">Marhova</span></p>
      <p class="person__role">Managing Director</p>
    </div>
    <span class="edge-band"></span>
  </section>
  <section class="card card--back" aria-label="Business card back">
    <div class="brand"><span>Corvana Flow</span><span class="brand__dot"></span></div>
  </section>
</main>
</body>
</html>
```